TrunvaX Calendar 2020 - Just need fine tuning

All design and content are ready. Just require some fine tuning
The date needs to be changed to 2020
and the address should be changed. I will provide new addresses.
Everything else can stay the same.

Other font styles liked:
• see file

Colors
a64599

```html
<!DOCTYPE html>
<html lang="en">
<head>
<meta charset="utf-8">
<title>TrunvaX Planner – January</title>
<link href="https://fonts.googleapis.com/css2?family=Open+Sans:wdth,wght@75..100,300..800&family=Oswald:wght@400&family=Playfair+Display:ital@1&family=Arimo&display=swap" rel="stylesheet">
<style>
  :root{
    --purple:#9a4f9e;
    --purple-deep:#8e3f93;
    --grey-text:#6b6b70;
    --panel:#e8eaed;
    --rule:#9a9a9a;
    --ink:#1a1a1a;
    --paper:#ffffff;
  }
  html,body{margin:0;padding:0;overflow:hidden;background:var(--paper);}
  .page{position:relative;width:729px;height:1200px;overflow:hidden;background:var(--paper);font-family:"Arimo",Arial,sans-serif;}
  .print-marks{position:absolute;inset:0;}
  .month-number{position:absolute;left:362px;top:138px;font-family:"Playfair Display",Georgia,serif;font-style:italic;font-size:78px;color:var(--purple);line-height:1;margin:0;font-weight:400;}
  .weekday{position:absolute;top:232px;width:129px;text-align:center;font-family:"Oswald",sans-serif;font-size:33px;color:var(--purple-deep);line-height:1;}
  .calendar-grid{position:absolute;left:0;top:0;}
  .day-number{position:absolute;font-size:23px;color:var(--grey-text);line-height:1;}
  .coupon{position:absolute;left:470px;top:67px;width:211px;height:1064px;background:var(--panel);}
  .coupon-ribbon{position:absolute;left:0;top:0;}
  .coupon-value{position:absolute;left:48px;top:78px;writing-mode:vertical-rl;font-family:"Open Sans",sans-serif;font-weight:800;font-size:104px;line-height:1;color:var(--paper);letter-spacing:-5px;}
  .coupon-percent{position:absolute;left:104px;top:210px;writing-mode:vertical-rl;font-family:"Open Sans",sans-serif;font-weight:800;font-size:44px;line-height:1;color:var(--paper);}
  .coupon-off{position:absolute;left:66px;top:212px;writing-mode:vertical-rl;font-family:"Open Sans",sans-serif;font-weight:800;font-size:26px;line-height:1;color:var(--paper);}
  .coupon-terms{position:absolute;left:54px;top:312px;width:104px;height:440px;writing-mode:vertical-rl;font-family:"Open Sans",sans-serif;color:var(--grey-text);}
  .coupon-headline{margin:0;font-size:40px;font-weight:800;line-height:44px;font-stretch:87%;white-space:nowrap;}
  .coupon-details{margin:0;font-size:18px;font-weight:300;line-height:20px;font-stretch:95%;white-space:nowrap;}
  .brand{position:absolute;left:128px;top:778px;writing-mode:vertical-rl;font-family:"Open Sans",sans-serif;font-weight:700;font-size:40px;line-height:1;color:var(--purple);}
  .brand-dot{display:inline-block;width:26px;height:26px;margin-top:8px;border-radius:50%;background:var(--purple);}
  .slug{position:absolute;top:1181px;font-size:11px;color:var(--ink);}
</style>
</head>
<body>
<div class="page">

  <svg class="print-marks" width="729" height="1200" viewBox="0 0 729 1200" aria-hidden="true">
    <g class="colour-bar-grey" stroke="#555" stroke-width="1.5">
      <rect x="8" y="0" width="28" height="31" fill="#000"/>
      <rect x="40" y="0" width="28" height="31" fill="#1b1b1b"/>
      <rect x="72" y="0" width="28" height="31" fill="#333"/>
      <rect x="104" y="0" width="28" height="31" fill="#4d4d4d"/>
      <rect x="136" y="0" width="28" height="31" fill="#666"/>
      <rect x="168" y="0" width="28" height="31" fill="#808080"/>
      <rect x="200" y="0" width="28" height="31" fill="#999"/>
      <rect x="232" y="0" width="28" height="31" fill="#b3b3b3"/>
      <rect x="264" y="0" width="28" height="31" fill="#ccc"/>
      <rect x="296" y="0" width="28" height="31" fill="#e6e6e6"/>
      <rect x="328" y="0" width="28" height="31" fill="#fff"/>
    </g>
    <g class="colour-bar-process" stroke="#555" stroke-width="1.5">
      <rect x="371" y="0" width="28" height="31" fill="#fff200"/>
      <rect x="403" y="0" width="28" height="31" fill="#ec008c"/>
      <rect x="435" y="0" width="28" height="31" fill="#00aeef"/>
      <rect x="467" y="0" width="28" height="31" fill="#2e3192"/>
      <rect x="499" y="0" width="28" height="31" fill="#00a651"/>
      <rect x="531" y="0" width="28" height="31" fill="#ed1c24"/>
      <rect x="563" y="0" width="28" height="31" fill="#231f20"/>
      <rect x="595" y="0" width="28" height="31" fill="#fff799"/>
      <rect x="627" y="0" width="28" height="31" fill="#f49ac1"/>
      <rect x="659" y="0" width="28" height="31" fill="#6dcff6"/>
      <rect x="691" y="0" width="28" height="31" fill="#939598"/>
    </g>
    <g class="crop-marks" stroke="#000" stroke-width="0.8">
      <line x1="48" y1="38" x2="48" y2="74"/><line x1="67" y1="38" x2="67" y2="74"/>
      <line x1="0" y1="66" x2="40" y2="66"/><line x1="0" y1="86" x2="40" y2="86"/>
      <line x1="661" y1="38" x2="661" y2="74"/><line x1="681" y1="38" x2="681" y2="74"/>
      <line x1="689" y1="66" x2="729" y2="66"/><line x1="689" y1="86" x2="729" y2="86"/>
      <line x1="48" y1="1124" x2="48" y2="1160"/><line x1="67" y1="1124" x2="67" y2="1160"/>
      <line x1="0" y1="1111" x2="40" y2="1111"/><line x1="0" y1="1131" x2="40" y2="1131"/>
      <line x1="661" y1="1124" x2="661" y2="1160"/><line x1="681" y1="1124" x2="681" y2="1160"/>
      <line x1="689" y1="1111" x2="729" y2="1111"/><line x1="689" y1="1131" x2="729" y2="1131"/>
    </g>
    <g class="registration-marks" stroke="#000" stroke-width="1" fill="none">
      <g transform="translate(365 56)"><circle r="9"/><circle r="5" fill="#000"/><line x1="-13" y1="0" x2="13" y2="0" stroke="#fff"/><line x1="0" y1="-13" x2="0" y2="13" stroke="#fff"/><line x1="-13" y1="0" x2="-5" y2="0"/><line x1="5" y1="0" x2="13" y2="0"/><line x1="0" y1="-13" x2="0" y2="-5"/><line x1="0" y1="5" x2="0" y2="13"/></g>
      <g transform="translate(365 1140)"><circle r="9"/><circle r="5" fill="#000"/><line x1="-13" y1="0" x2="13" y2="0" stroke="#fff"/><line x1="0" y1="-13" x2="0" y2="13" stroke="#fff"/><line x1="-13" y1="0" x2="-5" y2="0"/><line x1="5" y1="0" x2="13" y2="0"/><line x1="0" y1="-13" x2="0" y2="-5"/><line x1="0" y1="5" x2="0" y2="13"/></g>
      <g transform="translate(37 599)"><circle r="9"/><circle r="5" fill="#000"/><line x1="-13" y1="0" x2="13" y2="0" stroke="#fff"/><line x1="0" y1="-13" x2="0" y2="13" stroke="#fff"/><line x1="-13" y1="0" x2="-5" y2="0"/><line x1="5" y1="0" x2="13" y2="0"/><line x1="0" y1="-13" x2="0" y2="-5"/><line x1="0" y1="5" x2="0" y2="13"/></g>
      <g transform="translate(708 599)"><circle r="9"/><circle r="5" fill="#000"/><line x1="-13" y1="0" x2="13" y2="0" stroke="#fff"/><line x1="0" y1="-13" x2="0" y2="13" stroke="#fff"/><line x1="-13" y1="0" x2="-5" y2="0"/><line x1="5" y1="0" x2="13" y2="0"/><line x1="0" y1="-13" x2="0" y2="-5"/><line x1="0" y1="5" x2="0" y2="13"/></g>
    </g>
  </svg>

  <h1 class="month-number">01</h1>
  <div class="weekday" style="left:68px">Thu</div>
  <div class="weekday" style="left:197px">Fri</div>
  <div class="weekday" style="left:326px">Sat</div>

  <svg class="calendar-grid" width="729" height="1200" viewBox="0 0 729 1200" aria-hidden="true">
    <g stroke="var(--purple)" stroke-width="1.6">
      <line x1="77" y1="281" x2="466" y2="281"/>
      <line x1="77" y1="408" x2="466" y2="408"/>
      <line x1="77" y1="535" x2="466" y2="535"/>
      <line x1="77" y1="663" x2="466" y2="663"/>
      <line x1="77" y1="789" x2="466" y2="789"/>
      <line x1="77" y1="917" x2="466" y2="917"/>
      <line x1="206" y1="281" x2="206" y2="917"/>
      <line x1="335" y1="281" x2="335" y2="917"/>
      <line x1="47" y1="281" x2="59" y2="281"/>
      <line x1="47" y1="408" x2="59" y2="408"/>
      <line x1="47" y1="535" x2="59" y2="535"/>
      <line x1="47" y1="663" x2="59" y2="663"/>
      <line x1="47" y1="789" x2="59" y2="789"/>
      <line x1="47" y1="917" x2="59" y2="917"/>
    </g>
    <g class="note-lines" stroke="var(--rule)" stroke-width="0.8">
      <line x1="87" y1="964" x2="456" y2="964"/>
      <line x1="87" y1="995" x2="456" y2="995"/>
      <line x1="87" y1="1026" x2="456" y2="1026"/>
      <line x1="87" y1="1056" x2="456" y2="1056"/>
    </g>
    <line class="coupon-cut" x1="469" y1="67" x2="469" y2="1131" stroke="var(--ink)" stroke-width="2" stroke-dasharray="9 6"/>
  </svg>

  <span class="day-number" style="left:87px;top:291px">2</span>
  <span class="day-number" style="left:216px;top:291px">3</span>
  <span class="day-number" style="left:345px;top:291px">4</span>
  <span class="day-number" style="left:87px;top:418px">9</span>
  <span class="day-number" style="left:216px;top:418px">10</span>
  <span class="day-number" style="left:345px;top:418px">11</span>
  <span class="day-number" style="left:87px;top:545px">16</span>
  <span class="day-number" style="left:216px;top:545px">17</span>
  <span class="day-number" style="left:345px;top:545px">18</span>
  <span class="day-number" style="left:87px;top:673px">23</span>
  <span class="day-number" style="left:216px;top:673px">24</span>
  <span class="day-number" style="left:345px;top:673px">25</span>
  <span class="day-number" style="left:87px;top:799px">30</span>
  <span class="day-number" style="left:216px;top:799px">31</span>

  <aside class="coupon">
    <svg class="coupon-ribbon" width="211" height="320" viewBox="0 0 211 320" aria-hidden="true">
      <polygon points="0,0 211,0 211,310 97,259 0,298" fill="var(--purple)"/>
      <rect x="25" y="0" width="3.5" height="288" fill="var(--paper)"/>
      <rect x="165" y="0" width="3.5" height="290" fill="var(--paper)"/>
    </svg>
    <div class="coupon-value">20</div>
    <div class="coupon-percent">%</div>
    <div class="coupon-off">off</div>

    <div class="coupon-terms">
      <h2 class="coupon-headline">All accessories at 20% off</h2>
      <p class="coupon-details">with no minimum purchase (including masks, tubes, filters,<br>water chambers, etc). Please contact us for more details.<br>This coupon is valid for the entire month of January 2020.</p>
    </div>

    <div class="brand">TrunvaX<span class="brand-dot" aria-hidden="true"></span></div>
  </aside>

  <span class="slug" style="left:0">TrunvaX Planner.indd&nbsp;&nbsp;9</span>
  <span class="slug" style="right:2px">2018-10-31&nbsp;&nbsp;&nbsp;2:47 PM</span>
</div>
</body>
</html>
```